Billboard Design for Brightway Home Dentistry

Pinecrest Kinfolk Dental Care
Phone number: 318-572-0934
Address: 482 Coldbrook Blvd
Hours: 7am-5pm ; Monday-Friday

Dental Implant Surgery
Same Day Emergency Visits
Cosmetic Treatments
GLINT! Whitening

NAMES: Dr. Calvin Brastedder
Dr. Peter Haskell

MOST INSURANCES ACCEPTED

Eye catching slogan/colors/design for billboard

Our website is www.pinecrestkinfolkdentalcare.example to see current branding.

Target Market(s)

Target market is anyone in Alexandria. Focus on Families and High End Cosmetic Dentistry.

Industry/Entity Type

Dental Clinic

Requirements
Must have
• Pinecrest Kinfolk Dental Care
• Phone number: 318-572-0934
• Address: 482 Coldbrook Blvd
• Hours: 7am-5pm ; Monday-Friday
• Dental Implant Surgery
• Same Day Emergency Visits
• Cosmetic Treatments
• GLINT! Whitening
• NAMES: Dr. Calvin Brastedder
• Dr. Peter Haskell
• and logo
Nice to have
• digital billboard-try to catch attention with color or phrase
Should not have
• Can not make claims or compare to other area dentist's according to laws.

```html
<!DOCTYPE html>
<html lang="en">
<head>
<meta charset="utf-8">
<title>Pinecrest Kinfolk Dental Care Billboard</title>
<link rel="stylesheet" href="https://fonts.googleapis.com/css2?family=Oswald:wght@600;700&family=Montserrat:wght@500;700;800&display=swap">
<style>
  :root {
    --stage: #8a8a8a;
    --brand-blue: #1a3aa6;
    --brand-blue-deep: #0f2a8c;
    --ink: #1c1c1c;
    --paper: #ffffff;
    --rule: #9a9a9a;
    --placeholder: #c9d6e2;
  }
  * { margin: 0; padding: 0; box-sizing: border-box; }
  html, body { width: 1200px; height: 623px; overflow: hidden; }
  body {
    background: var(--stage);
    display: flex;
    align-items: center;
    justify-content: center;
  }
  .billboard {
    width: 1054px;
    height: 498px;
    background: var(--paper);
  }
  .billboard svg { display: block; width: 100%; height: 100%; }
  .title { font-family: "Oswald", sans-serif; font-weight: 700; fill: var(--brand-blue); }
  .doctors { font-family: "Montserrat", sans-serif; font-weight: 500; fill: var(--ink); }
  .service { font-family: "Montserrat", sans-serif; font-weight: 500; fill: var(--ink); }
  .hours-label { font-family: "Montserrat", sans-serif; font-weight: 800; fill: var(--ink); }
  .hours-value { font-family: "Oswald", sans-serif; font-weight: 600; fill: var(--brand-blue); }
  .insurance-text { font-family: "Montserrat", sans-serif; font-weight: 800; fill: var(--paper); }
  .phone { font-family: "Oswald", sans-serif; font-weight: 700; fill: var(--paper); }
  .address { font-family: "Montserrat", sans-serif; font-weight: 700; fill: var(--paper); }
  .brand-name { font-family: "Montserrat", sans-serif; font-weight: 800; fill: var(--brand-blue-deep); }
</style>
</head>
<body>
<main class="billboard">
  <svg viewBox="0 0 1318 623" xmlns="http://www.w3.org/2000/svg">
    <defs>
      <linearGradient id="pill-fill" x1="0" y1="0" x2="0" y2="1">
        <stop offset="0" stop-color="#3f63d6"/>
        <stop offset="0.5" stop-color="#1a3aa6"/>
        <stop offset="1" stop-color="#102a86"/>
      </linearGradient>
      <radialGradient id="pill-shadow">
        <stop offset="0" stop-color="#000" stop-opacity="0.35"/>
        <stop offset="1" stop-color="#000" stop-opacity="0"/>
      </radialGradient>
    </defs>

    <path class="photo-area" role="img" aria-label="Photo of a smiling family outdoors, a child riding on his father's shoulders"
          d="M0,0 H486 C560,150 570,430 500,623 H0 Z" fill="var(--placeholder)"/>

    <g class="brand">
      <circle cx="42" cy="72" r="14" fill="var(--brand-blue-deep)"/>
      <text class="brand-name" x="66" y="82" font-size="29">PINECREST KINFOLK</text>
      <text class="brand-name" x="66" y="112" font-size="22">DENTAL CARE</text>
    </g>

    <path class="swoosh-blue" fill="var(--brand-blue)"
          d="M496,0 H604 C664,160 654,430 526,623 H510 C580,430 572,150 496,0 Z"/>
    <path class="swoosh-edge" fill="var(--ink)"
          d="M604,0 H624 C684,160 672,420 546,623 H526 C654,430 664,160 604,0 Z"/>

    <path class="band-edge" fill="var(--ink)"
          d="M506,623 C640,500 880,412 1318,408 V428 C900,432 660,515 540,623 Z"/>
    <path class="band-blue" fill="var(--brand-blue)"
          d="M540,623 C660,520 900,445 1318,440 V623 Z"/>

    <text class="title" x="651" y="80" font-size="46" textLength="638" lengthAdjust="spacingAndGlyphs">PINECREST KINFOLK DENTAL CARE</text>
    <text class="doctors" x="651" y="118" font-size="23" textLength="638" lengthAdjust="spacingAndGlyphs">DR. CALVIN BRASTEDDER | DR. PETER HASKELL</text>

    <g class="services">
      <g transform="translate(664,186)">
        <circle r="7" fill="none" stroke="var(--brand-blue)" stroke-width="2"/>
        <path d="M-3,0 L-0.5,3 L5,-4" fill="none" stroke="var(--brand-blue)" stroke-width="2.2"/>
      </g>
      <text class="service" x="685" y="193" font-size="22">Dental Implant Surgery</text>
      <g transform="translate(664,217)">
        <circle r="7" fill="none" stroke="var(--brand-blue)" stroke-width="2"/>
        <path d="M-3,0 L-0.5,3 L5,-4" fill="none" stroke="var(--brand-blue)" stroke-width="2.2"/>
      </g>
      <text class="service" x="685" y="224" font-size="22">Same Day Emergency Visits</text>
      <g transform="translate(664,248)">
        <circle r="7" fill="none" stroke="var(--brand-blue)" stroke-width="2"/>
        <path d="M-3,0 L-0.5,3 L5,-4" fill="none" stroke="var(--brand-blue)" stroke-width="2.2"/>
      </g>
      <text class="service" x="685" y="255" font-size="22">Cosmetic Treatments</text>
      <g transform="translate(664,279)">
        <circle r="7" fill="none" stroke="var(--brand-blue)" stroke-width="2"/>
        <path d="M-3,0 L-0.5,3 L5,-4" fill="none" stroke="var(--brand-blue)" stroke-width="2.2"/>
      </g>
      <text class="service" x="685" y="286" font-size="22">GLINT! Whitening</text>
    </g>

    <line class="divider" x1="1008" y1="170" x2="1008" y2="296" stroke="var(--rule)" stroke-width="2"/>

    <g class="hours">
      <rect x="1023" y="188" width="265" height="103" fill="none" stroke="var(--rule)" stroke-width="2"/>
      <rect x="1070" y="176" width="171" height="24" fill="var(--paper)"/>
      <text class="hours-label" x="1155" y="195" font-size="19" text-anchor="middle">OPEN HOURS</text>
      <text class="hours-value" x="1155" y="235" font-size="31" text-anchor="middle">7AM-5PM</text>
      <text class="hours-value" x="1155" y="275" font-size="31" text-anchor="middle">MONDAY-FRIDAY</text>
    </g>

    <ellipse cx="975" cy="390" rx="300" ry="9" fill="url(#pill-shadow)"/>
    <rect class="insurance-pill" x="656" y="323" width="638" height="60" rx="30" fill="url(#pill-fill)"/>
    <text class="insurance-text" x="975" y="364" font-size="30" text-anchor="middle">MOST INSURANCES ACCEPTED</text>

    <g class="phone-icon" transform="translate(810,530)" fill="none" stroke="var(--paper)" stroke-width="2.4" stroke-linecap="round">
      <path d="M-10,-12 L-5,-14 L-1,-6 L-4,-3 C-2,2 2,6 6,8 L9,5 L16,9 L14,14 C4,16 -12,2 -10,-12 Z" fill="var(--paper)" stroke="none"/>
      <path d="M4,-12 A10,10 0 0 1 13,-3"/>
      <path d="M4,-19 A17,17 0 0 1 20,-3"/>
    </g>
    <text class="phone" x="853" y="558" font-size="76">318-572-0934</text>

    <g class="pin-icon" transform="translate(810,586)">
      <circle r="13" fill="none" stroke="var(--paper)" stroke-width="2"/>
      <path d="M0,8 C-4,2 -6,-1 -6,-3 A6,6 0 0 1 6,-3 C6,-1 4,2 0,8 Z" fill="var(--paper)"/>
      <circle cy="-3" r="2.2" fill="var(--brand-blue)"/>
    </g>
    <text class="address" x="853" y="595" font-size="27">482 Coldbrook Boulevard</text>
  </svg>
</main>
</body>
</html>
```